Simple 1 page layout for addrforge-tool.com

Visit http://addrforge-tool.com

The site calculates ipv6 unique local addresses for free. The content will stay as it is. There's going to be Brelvo promoslots below the red box and at the bottom of the page.

The red box contains the most important information on this page. The users focus should go there immediately.

The contents below composition is also kind of important.

Reason: I'm very busy at the moment. I need more time for evaluation and feedback. Thanks for your contributions and your patience.

Target Market(s)

IT and networking people

Industry/Entity Type

Brelvo

Requirements
Must have
• I need all pieces nicely cut, so I only have to do HTML and CSS.

```html
<!DOCTYPE html>
<html lang="en">
<head>
<meta charset="utf-8">
<title>Unique Local IPv6 – local network address generator</title>
<link rel="stylesheet" href="https://fonts.googleapis.com/css2?family=Arimo:wght@400;700&family=Cousine&display=swap">
<style>
:root{
  --page:#e6e6e6;
  --header-top:#f4f4f4;
  --header-bottom:#d9d9d9;
  --panel:#ffffff;
  --ink:#333333;
  --ink-soft:#555555;
  --muted:#777777;
  --brand-red:#c8102e;
  --ribbon-top:#d9232f;
  --ribbon-bottom:#b3121d;
  --ribbon-fold:#7a0a12;
  --blue-top:#3cb6ea;
  --blue-bottom:#1592cf;
  --blue-edge:#0d7bb4;
  --address-bar:#2a2a2a;
  --card-border:#dcdcdc;
  --link:#1a33c4;
  --url:#2a8a2a;
}
*{box-sizing:border-box;margin:0;padding:0}
html,body{width:1200px;height:2818px;overflow:hidden}
body{background:var(--page);font-family:"Arimo",Arial,sans-serif;color:var(--ink);position:relative}
.abs{position:absolute}

.site-header{left:0;top:0;width:1200px;height:176px;background:linear-gradient(var(--header-top),var(--header-bottom));border-bottom:1px solid #c9c9c9}
.site-title{left:42px;top:38px;font-size:36px;font-weight:400;color:#555;line-height:1}
.site-tagline{left:42px;top:80px;font-size:37px;color:var(--brand-red);line-height:1}
.share{left:843px;top:58px;display:flex;align-items:center;gap:12px;font-size:15px;color:#444}
.share-square{width:26px;height:22px;background:#d8d8d8;border:1px solid #bbb;border-radius:3px}

.panel{left:42px;top:216px;width:1111px;height:2519px;background:var(--panel);border-radius:10px;box-shadow:0 0 6px rgba(0,0,0,.12)}

.generator{left:122px;top:277px;width:958px;height:230px;background:linear-gradient(var(--blue-top),var(--blue-bottom));border:2px solid var(--blue-edge);border-radius:4px;box-shadow:0 3px 8px rgba(0,0,0,.25)}
.address{left:24px;top:17px;width:410px;height:56px;background:var(--address-bar);border-radius:4px;color:#fff;font-size:30px;line-height:56px;padding-left:18px}
.subnet-line{left:200px;font-size:21px;color:#fff}
.subnet-line span{margin-left:24px}

.ribbon{left:28px;height:38px;background:linear-gradient(var(--ribbon-top),var(--ribbon-bottom));color:#fff;font-size:19px;line-height:38px;padding-left:42px;clip-path:polygon(0 0,calc(100% - 16px) 0,100% 50%,calc(100% - 16px) 100%,0 100%)}
.ribbon-fold{left:28px;width:14px;height:10px;background:var(--ribbon-fold);clip-path:polygon(0 0,100% 0,100% 100%)}

.comp-label{left:103px;font-size:18px;color:var(--ink)}
.comp-value{font-size:14px;color:var(--ink-soft)}
.bit-table{left:441px;top:645px;font-family:"Cousine",monospace;font-size:14.5px;line-height:19px;white-space:pre;color:#222}

.faq-link{font-size:16px;color:var(--ink)}
.faq-link::before{content:"›";color:var(--blue-bottom);font-weight:700;margin-right:9px}

.intro{left:113px;top:1140px;font-size:16px;color:var(--ink-soft)}
.range-head{font-size:20px;color:var(--ink)}
.range-row{left:103px;font-size:15px;color:var(--ink-soft)}

.card{left:101px;width:1026px;background:#fff;border:1px solid var(--card-border);box-shadow:0 2px 5px rgba(0,0,0,.14);padding:26px 28px 0}
.card h3{font-size:20px;font-weight:400;color:var(--ink);margin-bottom:24px}
.card p{font-size:15px;line-height:21px;color:var(--ink-soft);margin-bottom:14px}

.ad-block{top:2489px;width:350px;height:212px;border:1px solid #e0e0e0;padding:6px 10px;font-size:13px;line-height:16px;color:#333}
.ad-block .by{position:absolute;right:10px;top:8px;font-size:12px;font-weight:700;color:#444}
.ad-title{color:var(--link);font-weight:700;text-decoration:underline;display:block;margin-top:2px}
.ad-url{color:var(--url);font-size:11px;display:block;margin-bottom:4px}

.footer{left:0;width:1200px;text-align:center;font-size:14px;color:#555}
</style>
</head>
<body>

<header class="abs site-header">
  <h1 class="abs site-title">Unique Local IPv6</h1>
  <p class="abs site-tagline">local network address generator</p>
  <div class="abs share"><span class="share-square"></span><span>+1 &nbsp;Recommend this on Brelvo</span></div>
</header>

<main class="abs panel"></main>

<section class="abs generator">
  <div class="abs address">fd52:6536:a2cb::/48</div>
  <p class="abs subnet-line" style="top:92px">1st 64-bit subnet<span>fd52:6536:a2cb::/64</span></p>
  <p class="abs subnet-line" style="top:139px">last 64-bit subnet<span>fd52:6536:a2cb:ffff::/64</span></p>
  <p class="abs subnet-line" style="top:186px">Just reload this page to get a new one</p>
</section>

<h2 class="abs ribbon" style="top:561px;width:329px;font-weight:400">COMPOSITION</h2>
<span class="abs ribbon-fold" style="top:599px"></span>

<p class="abs comp-label" style="top:624px">Prefix <span class="comp-value">fc::/7</span></p>
<p class="abs comp-label" style="top:659px">Local (L) <span class="comp-value">1</span></p>
<p class="abs comp-label" style="top:694px">Global ID</p>
<p class="abs comp-value" style="left:196px;top:697px;width:240px;text-align:center;line-height:17px">526536a2cb changes every time you visit this page</p>
<p class="abs comp-label" style="top:746px">Subnet ID <span class="comp-value">0 - ffff use freely for your own IPv6 subnetting</span></p>
<p class="abs comp-label" style="top:779px">Interface ID <span class="comp-value">Your host address.</span></p>
<div class="abs bit-table">| 7 bits |1|  40 bits   |  16 bits  |          64 bits           |
+--------+-+------------+-----------+----------------------------+
| Prefix |L| Global ID  | Subnet ID |        Interface ID        |
+--------+-+------------+-----------+----------------------------+</div>

<h2 class="abs ribbon" style="top:859px;width:207px;font-weight:400">F.A.Q.</h2>
<span class="abs ribbon-fold" style="top:897px"></span>

<nav>
  <p class="abs faq-link" style="left:146px;top:920px">What's a unique local address?</p>
  <p class="abs faq-link" style="left:146px;top:949px">What's the use?</p>
  <p class="abs faq-link" style="left:146px;top:978px">Why do they need to be unique?</p>
  <p class="abs faq-link" style="left:146px;top:1007px">Are they really globally unique?</p>
  <p class="abs faq-link" style="left:592px;top:920px">Isn't there an easy way?</p>
  <p class="abs faq-link" style="left:592px;top:949px">What is the subnet id?</p>
  <p class="abs faq-link" style="left:592px;top:978px">Where can I get more information?</p>
</nav>

<h2 class="abs ribbon" style="top:1071px;width:329px;font-weight:400">What's a unique local address?</h2>
<span class="abs ribbon-fold" style="top:1109px"></span>

<p class="abs intro">IPv6 unique local addresses are similar to the IPv4 private address classes with one big difference: THE ARE UNIQUE.</p>

<h3 class="abs range-head" style="left:103px;top:1206px;font-weight:400">IPv4 private addresses</h3>
<h3 class="abs range-head" style="left:465px;top:1206px;font-weight:400">IPv6 unique local addresses</h3>
<p class="abs range-row" style="top:1250px">Class A &nbsp;10.0.0.0/8</p>
<p class="abs range-row" style="top:1280px">Class B &nbsp;172.16.0.0/12</p>
<p class="abs range-row" style="top:1311px">Class C &nbsp;192.168.0.0/16</p>
<p class="abs range-row" style="left:465px;top:1254px;font-size:14px">fd::/48 - fd:ffff:ffff::/48</p>

<article class="abs card" style="top:1352px;height:179px">
  <h3>What's the use?</h3>
  <p>Local network addresses are used to make specific services only available for people and computers within your private network.</p>
  <p>For example if your company runs an intranet website containing confidential information about products, sales, customers or what so ever. This information might be vital for your employees to do their jobs, but you definitely don't want to make this website available publicly.</p>
</article>

<article class="abs card" style="top:1559px;height:193px">
  <h3>Why do they need to be unique?</h3>
  <p>Sometimes you want to join two or more private networks. A common example is when you connect your PC from your home network to your office network using a VPN. When both networks use the same private address range (e.g. 192.168.1.0/24) you only reach the office network during your VPN session as a result of a routing problem.</p>
</article>

<article class="abs card" style="top:1780px;height:192px">
  <h3>Are they really globally unique?</h3>
  <p>The global id part of unique local addresses is a randomly generated 40-bit integer. So there's a small possibility that two networks on this planet use the same unique local address. But there's a very little likelihood that this is ever going to happen. PROBABILITY: 1:1099511627776 or ~0.000000000001</p>
</article>

<article class="abs card" style="top:2000px;height:188px">
  <h3>Isn't there an easy way?</h3>
  <p>If you want to use a unique local network for your personal use or for testing only, no one bars you from using fd::/48, fd:abba::/48 or fd:1234::/48. But keep in mind there's are reason they have been made unique in the first place. And there's actually no good reason not to use a randomly generated address. How about that one on top of this page?</p>
</article>

<article class="abs card" style="top:2216px;height:146px">
  <h3>What is the subnet id?</h3>
  <p>After the global id you have 16 bits for your subnetting. Use them at will.</p>
  <p>If you don't have any subnetting plans right now, just start with 0000 (luckily you don't have to write that).</p>
</article>

<article class="abs card" style="top:2386px;height:84px;padding-top:20px">
  <h3 style="margin-bottom:18px">Where can I get more information?</h3>
  <p>RFC 4193</p>
</article>

<h2 class="abs ribbon" style="top:2573px;width:207px;font-weight:400">Brelvo Ads</h2>
<span class="abs ribbon-fold" style="top:2611px"></span>

<aside class="abs ad-block" style="left:383px">
  <span class="by">Ads by Brelvo</span>
  <span class="ad-title">Build a Video Community</span>
  Let your website users Encode and Upl<br>to your site
  <span class="ad-url">www.tealharbor-media.com</span>
  <span class="ad-title">Embedded Audio &amp; SBI?</span>
  QBX CubeUnit solutions in a box! +Video &amp; Audio DACs ADCs DAs &amp; more
  <span class="ad-url">www.quietbox-audio.com</span>
  <span class="ad-title">Embedding Video So Easy</span>
  This Thing Will Convert, Compress &amp; Embed Video In Web - Must See!
  <span class="ad-url">www.clipsimple-web.com</span>
</aside>

<aside class="abs ad-block" style="left:765px">
  <span class="by">Ads by Brelvo</span>
  <span class="ad-title">Build a Video Community</span>
  Let your website users Encode and Upl<br>to your site
  <span class="ad-url">www.tealharbor-media.com</span>
  <span class="ad-title">Embedded Audio &amp; SBI?</span>
  QBX CubeUnit solutions in a box! +Video &amp; Audio DACs ADCs DAs &amp; more
  <span class="ad-url">www.quietbox-audio.com</span>
  <span class="ad-title">Embedding Video So Easy</span>
  This Thing Will Convert, Compress &amp; Embed Video In Web - Must See!
  <span class="ad-url">www.clipsimple-web.com</span>
</aside>

<footer>
  <p class="abs footer" style="top:2753px">Terms and conditions &amp; Legal disclaimer</p>
  <p class="abs footer" style="top:2784px">Copyright © 2012 addrforge-tool</p>
</footer>

</body>
</html>
```